Redesign Video/PIcture Check in Page

Redesign our current TetherWatchApp iPhone App checkin screens - Keep the design simple so that programmers do not have to do too much extra work to make your design work. - Look at the attached website screenshot for the overall look and feel, and color scheme - Convert the attached vector logo to iOS Icon format. - Deliver all graphics in the density required for iPhone XS Max. I will upload current check in pages that need to be reimagined. Check in needs to be more intutitive. Would like to add some gamification to the verification screen where they currently are required to enter series of random numbers. simple card game etc might work better. See TetherWatchapp in itunes and google play store. also visit quorvant-link.example or tetherwatchapp.example for more information about our company.
The Current Checkin Process:
A. Client receives alert to checkin or submits voluntary checkin
B. Clicks checkin button on home Screen.
Redesign from here:
C. Clicks on a check in from check in list screen(new screen)
D. Enters verification number(gamification something better than random numbers)
E. Opens Camera
D. Takes Selfie
F. submits photo
G. clicks check in
SEE CURRENT STEPS PIC I UPLOADED

Target Market(s)

Courts,Probation and parole,Attorneys,Sheriffs,Jails, Alternative sentencing

Colors
3277b5

Requirements
Must have
• Must be easy to navigate,Intuitive!
Nice to have
• Gamification of check in verification.
• Step by step process with next button or similar

```html
<!DOCTYPE html>
<html lang="en">
<head>
<meta charset="utf-8">
<title>Voluntary Check-in Flow</title>
<link rel="stylesheet" href="https://fonts.googleapis.com/css2?family=Source+Sans+3:wght@400;600;700&display=swap">
<style>
:root{
  --page:#8f8f8f;
  --navy:#0b2e6e;
  --slate:#444b5b;
  --slate-line:#565d6c;
  --tabbar:#353a47;
  --panel:#b9bec7;
  --blue:#3277b5;
  --blue-bright:#3a86d2;
  --green:#2f9a39;
  --green-badge:#2e9a3b;
  --red:#d22a2a;
  --orange:#f26b1d;
  --white:#ffffff;
  --muted:#aab0bb;
  --ink:#2f3440;
}
*{box-sizing:border-box;margin:0;padding:0}
html,body{width:890px;height:1200px;overflow:hidden}
body{background:var(--page);font-family:"Source Sans 3",sans-serif;color:var(--white);position:relative}
.screen{position:absolute;width:254px;height:554px;background:var(--slate);border-radius:26px;overflow:hidden}
.col-1{left:36px}.col-2{left:318px}.col-3{left:600px}
.row-1{top:34px}.row-2{top:612px}
.status-bar{position:absolute;top:0;left:0;right:0;height:30px;background:var(--navy);font-size:7px;font-weight:600}
.status-bar .time{position:absolute;left:26px;top:14px}
.status-bar .signal{position:absolute;right:16px;top:13px}
.app-header{position:absolute;top:30px;left:0;right:0;height:26px;background:var(--navy);display:flex;align-items:center;justify-content:center;font-size:10.5px;font-weight:400;letter-spacing:.2px}
.app-header .menu{position:absolute;left:10px;top:8px}
.app-header .cancel,.app-header .back{position:absolute;top:9px;font-size:6px;font-weight:600;display:flex;align-items:center;gap:3px}
.app-header .cancel{right:10px}
.app-header .back{left:10px}
.checkin-list{position:absolute;top:56px;left:0;right:0;list-style:none}
.checkin-item{height:48.5px;border-bottom:1px solid var(--slate-line);padding:15px 0 0 10px;position:relative}
.checkin-item .date{font-size:7px;line-height:8px;display:block;margin-bottom:2px}
.checkin-item .title{font-size:10px;line-height:12px;font-weight:600;display:block}
.status-icon{position:absolute;right:12px;top:9px;width:30px;height:30px;border-radius:50%;border:2px solid var(--white);display:flex;align-items:center;justify-content:center}
.status-icon.ok{background:var(--green-badge)}
.status-icon.fail{background:var(--red)}
.status-icon.next{background:var(--blue-bright);border:none}
.step-head{position:absolute;top:96px;left:0;right:0;text-align:center}
.step-head .date{font-size:7px;line-height:8px;display:block;margin-bottom:4px}
.step-head .title{font-size:12.5px;line-height:15px;font-weight:600;display:block}
.stepper{display:flex;justify-content:center;align-items:center;margin-top:5px}
.stepper .line{width:8px;height:1px;background:var(--white)}
.stepper .dot{width:14px;height:14px;border-radius:50%;border:1px solid var(--white);font-size:7px;display:flex;align-items:center;justify-content:center}
.stepper .dot.current{background:var(--muted);color:var(--ink);border-color:var(--muted)}
.stepper .dot.done{background:var(--white)}
.game-board{position:absolute;left:10px;top:156px;width:234px;height:221px;background:var(--panel);border-radius:8px}
.game-board svg{position:absolute;left:16px;top:10px}
.prompt{position:absolute;top:389px;left:0;right:0;text-align:center;font-size:10px;font-weight:600}
.action{position:absolute;top:408px;width:53px;height:53px;border-radius:50%;background:var(--blue-bright);display:flex;align-items:center;justify-content:center}
.selfie-frame{position:absolute;left:17px;top:156px;width:221px;height:221px;background:linear-gradient(160deg,#b47a5e,#c8a592 55%,#7c9cc0);}
.selfie-frame .guide-h,.selfie-frame .guide-v{position:absolute;border-color:rgba(255,255,255,.8);border-style:dashed}
.preview-panel{position:absolute;left:10px;top:156px;width:234px;height:221px;background:var(--panel);border-radius:8px}
.preview-photo{position:absolute;left:31px;top:20px;width:172px;height:171px;background:linear-gradient(160deg,#b47a5e,#c8a592 55%,#7c9cc0)}
.retake{position:absolute;left:0;right:0;bottom:13px;text-align:center;font-size:7px;color:var(--ink);font-weight:600;display:flex;justify-content:center;align-items:center;gap:3px}
.success-panel{position:absolute;top:56px;left:0;right:0;bottom:58px;background:var(--green);text-align:center}
.brand-name{position:absolute;left:0;right:0;top:170px;font-size:16px;font-weight:700;letter-spacing:1.5px}
.success-title{position:absolute;top:252px;left:0;right:0;font-size:20px;line-height:22px;font-weight:700}
.success-text{position:absolute;top:274px;left:0;right:0;font-size:10px;line-height:12px;font-weight:600}
.ok-button{position:absolute;top:299px;left:103px;width:48px;height:18px;border:1.5px solid var(--white);border-radius:9px;font-size:8px;font-weight:700;line-height:15px}
.tab-bar{position:absolute;left:0;right:0;bottom:0;height:58px;background:var(--tabbar);display:flex;justify-content:space-around;padding-top:10px}
.tab{width:50px;text-align:center;font-size:5.5px;font-weight:700;position:relative}
.tab svg{display:block;margin:0 auto 3px}
.tab.inactive{color:var(--muted)}
.tab .badge{position:absolute;left:30px;top:-3px;background:var(--orange);font-size:6px;width:9px;height:9px;line-height:9px;color:var(--white)}
.home-indicator{position:absolute;bottom:5px;left:86px;width:82px;height:3px;border-radius:2px;background:var(--white)}
</style>
</head>
<body>

<svg width="0" height="0" style="position:absolute">
  <defs>
    <symbol id="i-tick" viewBox="0 0 20 20"><path d="M5 10.5l3.5 3.5L15 7" fill="none" stroke="#fff" stroke-width="2.6" stroke-linecap="round" stroke-linejoin="round"/></symbol>
    <symbol id="i-cross" viewBox="0 0 20 20"><path d="M6 6l8 8M14 6l-8 8" fill="none" stroke="#fff" stroke-width="2.6" stroke-linecap="round"/></symbol>
    <symbol id="i-home" viewBox="0 0 20 20"><path d="M3 9l7-6 7 6v8h-5v-5H8v5H3z" fill="none" stroke="currentColor" stroke-width="1.6" stroke-linejoin="round"/></symbol>
    <symbol id="i-pin" viewBox="0 0 20 20"><path d="M10 18s-6-6-6-10a6 6 0 0112 0c0 4-6 10-6 10z" fill="none" stroke="currentColor" stroke-width="1.5"/><path d="M7.3 8.2l2 2 3.5-3.5" fill="none" stroke="currentColor" stroke-width="1.5"/></symbol>
    <symbol id="i-map" viewBox="0 0 20 20"><circle cx="10" cy="10" r="5.5" fill="none" stroke="currentColor" stroke-width="1.5"/><circle cx="10" cy="10" r="1.8" fill="currentColor"/><path d="M10 1.5v3M10 15.5v3M1.5 10h3M15.5 10h3" stroke="currentColor" stroke-width="1.5"/></symbol>
    <symbol id="i-info" viewBox="0 0 20 20"><circle cx="10.5" cy="3.5" r="1.6" fill="currentColor"/><path d="M8 8h3v8.5M7.5 16.5h6" fill="none" stroke="currentColor" stroke-width="1.6"/></symbol>
    <symbol id="i-menu" viewBox="0 0 12 10"><path d="M0 1h12M0 5h12M0 9h12" stroke="#fff" stroke-width="1.2"/></symbol>
    <symbol id="i-cancel" viewBox="0 0 10 10"><circle cx="5" cy="5" r="4.3" fill="none" stroke="#fff" stroke-width="1"/><path d="M3.3 3.3l3.4 3.4M6.7 3.3L3.3 6.7" stroke="#fff" stroke-width="1"/></symbol>
    <symbol id="i-signal" viewBox="0 0 36 8"><rect x="0" y="5" width="2" height="3" fill="#fff"/><rect x="3" y="3.5" width="2" height="4.5" fill="#fff"/><rect x="6" y="2" width="2" height="6" fill="#fff"/><rect x="9" y="0.5" width="2" height="7.5" fill="#fff"/><path d="M14 3a6 6 0 018 0M15.5 5a3.6 3.6 0 015 0" fill="none" stroke="#fff" stroke-width="1"/><circle cx="18" cy="7" r=".9" fill="#fff"/><rect x="25" y="1.5" width="10" height="5" rx="1.2" fill="#fff"/></symbol>
  </defs>
</svg>

<!-- Screen: check-in list with pending request -->
<section class="screen col-1 row-1">
  <div class="status-bar"><span class="time">5:30</span><svg class="signal" width="36" height="8"><use href="#i-signal"/></svg></div>
  <header class="app-header"><svg class="menu" width="12" height="10"><use href="#i-menu"/></svg>CHECK-IN</header>
  <ul class="checkin-list">
    <li class="checkin-item"><span class="date">01 Nov 2018 12:11:16</span><span class="title">Voluntary Check-in Request</span><span class="status-icon next"><svg width="16" height="16" viewBox="0 0 16 16"><path d="M2 2l13 6-13 6 3-6z" fill="#fff"/></svg></span></li>
    <li class="checkin-item"><span class="date">30 Oct 2018 14:50:23</span><span class="title">Voluntary Check-in Request</span><span class="status-icon ok"><svg width="18" height="18"><use href="#i-tick"/></svg></span></li>
    <li class="checkin-item"><span class="date">29 Oct 2018 16:49:54</span><span class="title">Voluntary Check-in Request</span><span class="status-icon ok"><svg width="18" height="18"><use href="#i-tick"/></svg></span></li>
    <li class="checkin-item"><span class="date">27 Oct 2018 10:51:39</span><span class="title">Voluntary Check-in Request</span><span class="status-icon fail"><svg width="18" height="18"><use href="#i-cross"/></svg></span></li>
    <li class="checkin-item"><span class="date">27 Oct 2018 10:49:27</span><span class="title">Voluntary Check-in Request</span><span class="status-icon ok"><svg width="18" height="18"><use href="#i-tick"/></svg></span></li>
    <li class="checkin-item"><span class="date">26 Oct 2018 17:59:50</span><span class="title">Voluntary Check-in Request</span><span class="status-icon ok"><svg width="18" height="18"><use href="#i-tick"/></svg></span></li>
    <li class="checkin-item"><span class="date">26 Oct 2018 17:58:44</span><span class="title">Voluntary Check-in Request</span><span class="status-icon ok"><svg width="18" height="18"><use href="#i-tick"/></svg></span></li>
    <li class="checkin-item"><span class="date">24 Oct 2018 23:56:36</span><span class="title">Voluntary Check-in Request</span><span class="status-icon ok"><svg width="18" height="18"><use href="#i-tick"/></svg></span></li>
    <li class="checkin-item"><span class="date">20 Oct 2018 10:47:59</span><span class="title">Voluntary Check-in Request</span><span class="status-icon fail"><svg width="18" height="18"><use href="#i-cross"/></svg></span></li>
  </ul>
  <nav class="tab-bar">
    <div class="tab"><svg width="16" height="16"><use href="#i-home"/></svg>HOME</div>
    <div class="tab inactive"><svg width="16" height="16"><use href="#i-pin"/></svg>CHECK-INS<span class="badge">5</span></div>
    <div class="tab"><svg width="16" height="16"><use href="#i-map"/></svg>MAP</div>
    <div class="tab"><svg width="16" height="16"><use href="#i-info"/></svg>HOW TO</div>
  </nav>
  <div class="home-indicator"></div>
</section>

<!-- Screen: step 1 game verification -->
<section class="screen col-2 row-1">
  <div class="status-bar"><span class="time">5:30</span><svg class="signal" width="36" height="8"><use href="#i-signal"/></svg></div>
  <header class="app-header"><svg class="menu" width="12" height="10"><use href="#i-menu"/></svg>CHECK-IN<span class="cancel"><svg width="9" height="9"><use href="#i-cancel"/></svg>CANCEL</span></header>
  <div class="step-head"><span class="date">01 Nov 2018 12:11:16</span><span class="title">Voluntary Check-in Request</span>
    <div class="stepper"><span class="line"></span><span class="dot current">1</span><span class="line"></span><span class="dot">2</span><span class="line"></span><span class="dot">3</span><span class="line"></span></div>
  </div>
  <div class="game-board">
    <svg width="202" height="202" viewBox="0 0 202 202">
      <rect x="0" y="0" width="67" height="67" fill="#fff"/>
      <circle cx="21" cy="33" r="5" fill="none" stroke="#8a909b" stroke-width="1.2"/>
      <text x="30" y="35.5" font-size="5" fill="#8a909b" font-family="Source Sans 3, sans-serif">OR</text>
      <path d="M40 28l9 10M49 28l-9 10" stroke="#8a909b" stroke-width="1.2"/>
      <path d="M67 0v202M134 0v202M0 67h202M0 134h202" stroke="#3c4250" stroke-width="1"/>
      <path d="M85 85l31 31M116 85l-31 31M152 152l31 31M183 152l-31 31" stroke="#3c4250" stroke-width="3"/>
      <circle cx="33.5" cy="167.5" r="17" fill="none" stroke="#3c4250" stroke-width="3"/>
      <circle cx="100.5" cy="167.5" r="17" fill="none" stroke="#3c4250" stroke-width="3"/>
    </svg>
  </div>
  <p class="prompt">Let's win!</p>
  <span class="action" style="left:69px"><svg width="28" height="28"><circle cx="14" cy="14" r="11" fill="none" stroke="#fff" stroke-width="2.4"/></svg></span>
  <span class="action" style="left:131px"><svg width="28" height="28"><path d="M4 4l20 20M24 4L4 24" stroke="#fff" stroke-width="2.4"/></svg></span>
  <nav class="tab-bar">
    <div class="tab"><svg width="16" height="16"><use href="#i-home"/></svg>HOME</div>
    <div class="tab inactive"><svg width="16" height="16"><use href="#i-pin"/></svg>CHECK-INS<span class="badge">5</span></div>
    <div class="tab"><svg width="16" height="16"><use href="#i-map"/></svg>MAP</div>
    <div class="tab"><svg width="16" height="16"><use href="#i-info"/></svg>HOW TO</div>
  </nav>
  <div class="home-indicator"></div>
</section>

<!-- Screen: step 2 camera -->
<section class="screen col-3 row-1">
  <div class="status-bar"><span class="time">5:30</span><svg class="signal" width="36" height="8"><use href="#i-signal"/></svg></div>
  <header class="app-header"><svg class="menu" width="12" height="10"><use href="#i-menu"/></svg>CHECK-IN<span class="cancel"><svg width="9" height="9"><use href="#i-cancel"/></svg>CANCEL</span></header>
  <div class="step-head"><span class="date">01 Nov 2018 12:11:16</span><span class="title">Voluntary Check-in Request</span>
    <div class="stepper"><span class="line"></span><span class="dot done"><svg width="10" height="10" viewBox="0 0 20 20"><path d="M5 10.5l3.5 3.5L15 7" fill="none" stroke="#2f3440" stroke-width="3"/></svg></span><span class="line"></span><span class="dot current">2</span><span class="line"></span><span class="dot">3</span><span class="line"></span></div>
  </div>
  <div class="selfie-frame" role="img" aria-label="Live camera view of the client's selfie against a brick wall">
    <span class="guide-v" style="left:110px;top:0;bottom:0;border-width:0 0 0 1px"></span>
    <span class="guide-h" style="top:74px;left:0;right:0;border-width:1px 0 0 0"></span>
    <span class="guide-h" style="top:147px;left:0;right:0;border-width:1px 0 0 0"></span>
  </div>
  <p class="prompt">Please take your photo.</p>
  <span class="action" style="left:100px"><svg width="28" height="24" viewBox="0 0 28 24"><path d="M3 6h6l2-3h6l2 3h6v15H3z" fill="#fff"/><circle cx="14" cy="13" r="5" fill="#3a86d2"/><circle cx="14" cy="13" r="3" fill="#fff"/></svg></span>
  <nav class="tab-bar">
    <div class="tab"><svg width="16" height="16"><use href="#i-home"/></svg>HOME</div>
    <div class="tab inactive"><svg width="16" height="16"><use href="#i-pin"/></svg>CHECK-INS<span class="badge">5</span></div>
    <div class="tab"><svg width="16" height="16"><use href="#i-map"/></svg>MAP</div>
    <div class="tab"><svg width="16" height="16"><use href="#i-info"/></svg>HOW TO</div>
  </nav>
  <div class="home-indicator"></div>
</section>

<!-- Screen: step 3 confirm check-in -->
<section class="screen col-1 row-2">
  <div class="status-bar"><span class="time">5:30</span><svg class="signal" width="36" height="8"><use href="#i-signal"/></svg></div>
  <header class="app-header"><span class="back"><svg width="6" height="9" viewBox="0 0 6 9"><path d="M5 1L1.5 4.5 5 8" fill="none" stroke="#fff" stroke-width="1.2"/></svg>BACK</span>CHECK-IN<span class="cancel"><svg width="9" height="9"><use href="#i-cancel"/></svg>CANCEL</span></header>
  <div class="step-head"><span class="date">01 Nov 2018 12:11:16</span><span class="title">Voluntary Check-in Request</span>
    <div class="stepper"><span class="line"></span><span class="dot done"><svg width="10" height="10" viewBox="0 0 20 20"><path d="M5 10.5l3.5 3.5L15 7" fill="none" stroke="#2f3440" stroke-width="3"/></svg></span><span class="line"></span><span class="dot done"><svg width="10" height="10" viewBox="0 0 20 20"><path d="M5 10.5l3.5 3.5L15 7" fill="none" stroke="#2f3440" stroke-width="3"/></svg></span><span class="line"></span><span class="dot current">3</span><span class="line"></span></div>
  </div>
  <div class="preview-panel">
    <div class="preview-photo" role="img" aria-label="Captured selfie of the client for review"></div>
    <div class="retake"><svg width="9" height="7" viewBox="0 0 28 24"><path d="M3 6h6l2-3h6l2 3h6v15H3z" fill="#2f3440"/><circle cx="14" cy="13" r="4" fill="#b9bec7"/></svg>RETAKE</div>
  </div>
  <p class="prompt">Please check-in.</p>
  <span class="action" style="left:100px"><svg width="26" height="30" viewBox="0 0 20 24"><path d="M10 23s-8-7-8-13a8 8 0 0116 0c0 6-8 13-8 13z" fill="#fff"/><path d="M6 10l3 3 5-5" fill="none" stroke="#3a86d2" stroke-width="2.2"/></svg></span>
  <nav class="tab-bar">
    <div class="tab"><svg width="16" height="16"><use href="#i-home"/></svg>HOME</div>
    <div class="tab inactive"><svg width="16" height="16"><use href="#i-pin"/></svg>CHECK-INS<span class="badge">5</span></div>
    <div class="tab"><svg width="16" height="16"><use href="#i-map"/></svg>MAP</div>
    <div class="tab"><svg width="16" height="16"><use href="#i-info"/></svg>HOW TO</div>
  </nav>
  <div class="home-indicator"></div>
</section>

<!-- Screen: success -->
<section class="screen col-2 row-2">
  <div class="status-bar"><span class="time">5:30</span><svg class="signal" width="36" height="8"><use href="#i-signal"/></svg></div>
  <header class="app-header"><svg class="menu" width="12" height="10"><use href="#i-menu"/></svg>CHECK-IN</header>
  <div class="success-panel">
    <p class="brand-name">QUORVANT</p>
    <p class="success-title">SUCCESS!</p>
    <p class="success-text">Check-in complete. Thank you.</p>
    <div class="ok-button">OK</div>
  </div>
  <nav class="tab-bar">
    <div class="tab"><svg width="16" height="16"><use href="#i-home"/></svg>HOME</div>
    <div class="tab inactive"><svg width="16" height="16"><use href="#i-pin"/></svg>CHECK-INS<span class="badge">4</span></div>
    <div class="tab"><svg width="16" height="16"><use href="#i-map"/></svg>MAP</div>
    <div class="tab"><svg width="16" height="16"><use href="#i-info"/></svg>HOW TO</div>
  </nav>
  <div class="home-indicator"></div>
</section>

<!-- Screen: updated check-in list -->
<section class="screen col-3 row-2">
  <div class="status-bar"><span class="time">5:30</span><svg class="signal" width="36" height="8"><use href="#i-signal"/></svg></div>
  <header class="app-header"><svg class="menu" width="12" height="10"><use href="#i-menu"/></svg>CHECK-IN</header>
  <ul class="checkin-list">
    <li class="checkin-item"><span class="date">01 Nov 2018 12:11:16</span><span class="title">Voluntary Check-in Request</span><span class="status-icon ok"><svg width="18" height="18"><use href="#i-tick"/></svg></span></li>
    <li class="checkin-item"><span class="date">30 Oct 2018 14:50:23</span><span class="title">Voluntary Check-in Request</span><span class="status-icon ok"><svg width="18" height="18"><use href="#i-tick"/></svg></span></li>
    <li class="checkin-item"><span class="date">29 Oct 2018 16:49:54</span><span class="title">Voluntary Check-in Request</span><span class="status-icon ok"><svg width="18" height="18"><use href="#i-tick"/></svg></span></li>
    <li class="checkin-item"><span class="date">27 Oct 2018 10:51:39</span><span class="title">Voluntary Check-in Request</span><span class="status-icon fail"><svg width="18" height="18"><use href="#i-cross"/></svg></span></li>
    <li class="checkin-item"><span class="date">27 Oct 2018 10:49:27</span><span class="title">Voluntary Check-in Request</span><span class="status-icon ok"><svg width="18" height="18"><use href="#i-tick"/></svg></span></li>
    <li class="checkin-item"><span class="date">26 Oct 2018 17:59:50</span><span class="title">Voluntary Check-in Request</span><span class="status-icon ok"><svg width="18" height="18"><use href="#i-tick"/></svg></span></li>
    <li class="checkin-item"><span class="date">26 Oct 2018 17:58:44</span><span class="title">Voluntary Check-in Request</span><span class="status-icon ok"><svg width="18" height="18"><use href="#i-tick"/></svg></span></li>
    <li class="checkin-item"><span class="date">24 Oct 2018 23:56:36</span><span class="title">Voluntary Check-in Request</span><span class="status-icon ok"><svg width="18" height="18"><use href="#i-tick"/></svg></span></li>
    <li class="checkin-item"><span class="date">20 Oct 2018 10:47:59</span><span class="title">Voluntary Check-in Request</span><span class="status-icon fail"><svg width="18" height="18"><use href="#i-cross"/></svg></span></li>
  </ul>
  <nav class="tab-bar">
    <div class="tab"><svg width="16" height="16"><use href="#i-home"/></svg>HOME</div>
    <div class="tab inactive"><svg width="16" height="16"><use href="#i-pin"/></svg>CHECK-INS<span class="badge">4</span></div>
    <div class="tab"><svg width="16" height="16"><use href="#i-map"/></svg>MAP</div>
    <div class="tab"><svg width="16" height="16"><use href="#i-info"/></svg>HOW TO</div>
  </nav>
  <div class="home-indicator"></div>
</section>

</body>
</html>
```